Upgrade 4 Images - Bid 1, then we can discuss the other 3

We have a four graphics that we use in various presentations and business proposals. We want to upgrade them to make them really pop and match the level of service we provide, without going overboard.

We're open to new ideas, but the general form and content should stay the same.

I'd like to have all four designed by the same person, but I'm assuming this bid will be for 1 of the four, and then the other three can be contracted as additions.

```html
<!DOCTYPE html>
<html lang="en">
<head>
<meta charset="utf-8">
<title>Operating Quadrants – Data Processing as a Service</title>
<link rel="stylesheet" href="https://fonts.googleapis.com/css2?family=Nunito+Sans:wght@400;600&display=swap">
<style>
  :root {
    --navy: #24275a;
    --navy-deep: #15173a;
    --band-dark: #1b1a35;
    --orange: #f4812b;
    --white: #ffffff;
    --font-main: "Nunito Sans", "Avenir Next", sans-serif;
  }
  html, body {
    margin: 0;
    padding: 0;
    width: 1200px;
    height: 675px;
    overflow: hidden;
    background: var(--navy-deep);
  }
  .slide {
    position: relative;
    width: 1200px;
    height: 675px;
    overflow: hidden;
    font-family: var(--font-main);
  }
  .slide-backdrop {
    position: absolute;
    inset: 0;
    background:
      radial-gradient(ellipse at 55% 40%, #343a74 0%, rgba(36,39,90,0) 60%),
      linear-gradient(180deg, #2a2e66 0%, var(--navy) 45%, var(--navy-deep) 100%);
  }
  .slide-title {
    position: absolute;
    top: 38px;
    left: 0;
    width: 1197px;
    margin: 0;
    text-align: center;
    font-weight: 400;
    font-size: 47px;
    letter-spacing: 1px;
    line-height: 1;
    color: var(--white);
  }
  .slide-subtitle {
    position: absolute;
    top: 92px;
    left: 0;
    width: 1180px;
    margin: 0;
    text-align: center;
    font-weight: 400;
    font-size: 29px;
    line-height: 1;
    color: var(--orange);
  }
  .quadrant-diagram {
    position: absolute;
    inset: 0;
    width: 1200px;
    height: 675px;
  }
  .band { fill: var(--orange); }
  .axis { fill: var(--band-dark); }
  .quadrant-label {
    font-family: var(--font-main);
    font-size: 44px;
    fill: var(--white);
    text-anchor: middle;
    dominant-baseline: central;
  }
  .axis-label {
    font-family: var(--font-main);
    font-size: 22px;
    fill: var(--orange);
    text-anchor: middle;
    dominant-baseline: central;
  }
  .zone-label {
    font-family: var(--font-main);
    font-size: 30px;
    fill: var(--white);
    text-anchor: middle;
  }
  .brand-name {
    position: absolute;
    left: 42px;
    top: 512px;
    margin: 0;
    font-weight: 600;
    font-size: 30px;
    line-height: 1.1;
    color: var(--orange);
  }
  .brand-name span { display: block; }
  .site-url {
    position: absolute;
    left: 944px;
    top: 608px;
    margin: 0;
    font-size: 16px;
    letter-spacing: 1px;
    color: var(--white);
  }
</style>
</head>
<body>
<main class="slide">
  <div class="slide-backdrop" role="img" aria-label="Darkened navy-tinted photo of a business team meeting with a presenter beside a screen showing analysis charts"></div>

  <h1 class="slide-title">OPERATIN QUADRANTS</h1>
  <p class="slide-subtitle">Data Processing as a Service</p>

  <svg class="quadrant-diagram" viewBox="0 0 1500 844" aria-label="Operating quadrants diagram">
    <!-- axes -->
    <polygon class="axis" points="733,228 758,200 783,228 783,733 758,761 733,733"/>
    <polygon class="axis" points="500,452 1010,452 1035,477.5 1010,503 500,503 475,477.5"/>

    <!-- quadrant bands -->
    <polygon class="band" points="488,433 713,208 733,228 733,266 547,452 507,452"/>
    <polygon class="band" points="1027,433 802,208 782,228 782,266 968,452 1008,452"/>
    <polygon class="band" points="488,522 713,747 733,727 733,689 547,503 507,503"/>
    <polygon class="band" points="1027,522 802,747 782,727 782,689 968,503 1008,503"/>

    <!-- quadrant names -->
    <text class="quadrant-label" transform="translate(622,342) rotate(-45)">Specialist</text>
    <text class="quadrant-label" transform="translate(893,342) rotate(45)">Enterprise</text>
    <text class="quadrant-label" transform="translate(622,622) rotate(45)">Ad Hoc</text>
    <text class="quadrant-label" transform="translate(888,612) rotate(-45)">Factory</text>

    <!-- axis names -->
    <text class="axis-label" transform="translate(758,310) rotate(-90)">High Maturity</text>
    <text class="axis-label" transform="translate(758,653) rotate(90)">Low Maturity</text>
    <text class="axis-label" x="589" y="478">Low Utilization</text>
    <text class="axis-label" x="924" y="476">High Utilization</text>

    <!-- centre -->
    <g transform="translate(750,478) rotate(-40)">
      <text class="zone-label" x="0" y="-4">Goldilocks</text>
      <text class="zone-label" x="0" y="30">Zone</text>
    </g>
  </svg>

  <p class="brand-name"><span>The</span><span>Korvane</span><span>Group</span></p>
  <p class="site-url">www.korvanegroup.com</p>
</main>
</body>
</html>
```